New Business Card Design Project

The idea, the card is to put a card, which contains two companies at the same time. Please see the attached data and idea of how the current cards are.
VELMIR
Constructora
Ferrepiezas Caliza SRL.
Equipos para Plantas de Tratamientos y Acueductos, Alquiler de Equipos Pesados para la Construcción.
C / Tomás Urbina No.47
Barrio Lucero, Santo Domingo. República Dominicana.
Tel .: 1809 512 4476
CEL: 1829 746 2158
oriol@ferrepiezascaliza.example
velmirconstrution@correo-ejemplo.example
www.ferrepiezascaliza.example
Velmir construction.
Es una empresa constructora.
NOTA: La idea es llevar una sola tarjeta para dos compañías. o si no resulta hacer un diseño en cada lado, uno para cada empresa.Equipos para Plantas de Tratamiento y Acueductos, Alquiler de Equipos Pesados para la Construcción.
Deben de llevar, los logos.
VELMIR
Constructora
Ferrepiezas Caliza SRL.
C / Tomás Urbina No.47
Tel .: 1809 512 4476
CEL: 1829 746 2158
Velmir construction.
VELMIR
Constructora
Ferrepiezas Caliza SRL.
C / Tomás Urbina No.47
Tel .: 1809 512 4476
CEL: 1829 746 2158
Velmir construction.
It is a construction company
NOTE: The idea is to carry a single card for two companies. or if it does not turn out to make a design on each side, one for each company. Equipment for Treatment Plants and Aqueducts, Rental of Heavy Equipment for Construction.
They must carry, the logos.
How is the design similar to that, send example, for data, from previous designs.
What I'm looking for is a new design, not a remodeled copy
ferrepiezascaliza
Tel: 1809 542 4476
cel: 1829 746 2158
oriol@gerrepiezascaliza.example
Direccion:
C/ Tomás Urbina # 47
Barrio lucero, Santo Domingo
Republica Dominicana
Velmir
constructora
Tel: 1809 358-1047
Cel: 1829 746 2158
velmirsa1@correo-ejemplo.example
Direccion:
C/ Tomás Urbina # 47
Republica Dominicana
FERREPIEZAS CALIZA, S.R.L.
C/ Ramiro Olmedo Lasta esquina Tomás Urbina # 47
Barrio Lucero, Santo Domingo, República Dominicana
Office: 809.542.4476
Fax: 809.594.7361
Cel (Local): 829 746 2158
E-mail: MUESTRA@MUESTRA.example
E-mail:MUESTRA@correo-ejemplo.example
Website: http://www.MUESTRA.example

```html
<!DOCTYPE html>
<html lang="es">
<head>
<meta charset="utf-8">
<title>Velmir Constructora – Tarjeta de presentación</title>
<link rel="stylesheet" href="https://fonts.googleapis.com/css2?family=Work+Sans:wght@400;500;800&display=swap">
<style>
  :root {
    --backdrop: #a9a9a9;
    --card: #3b3b3d;
    --white: #ffffff;
    --yellow: #f5c518;
    --text-soft: #ececec;
  }
  * { box-sizing: border-box; margin: 0; padding: 0; }
  html, body { width: 1200px; height: 930px; overflow: hidden; }
  body {
    background: var(--backdrop);
    font-family: "Work Sans", sans-serif;
    position: relative;
  }
  .card {
    position: absolute;
    width: 540px;
    height: 310px;
    background: var(--card);
    border-radius: 22px;
    box-shadow: 0 10px 24px rgba(0,0,0,.28);
    color: var(--white);
  }
  .card--front { left: 50px; top: 140px; }
  .card--back { left: 610px; top: 480px; }

  .brand {
    position: absolute;
    display: flex;
    align-items: center;
    gap: 12px;
  }
  .brand__mark { background: var(--yellow); display: block; }
  .brand__name { font-weight: 800; color: var(--white); letter-spacing: .01em; line-height: 1; }

  .card--front .brand { left: 50%; top: 50%; transform: translate(-50%, -50%); }
  .card--front .brand__mark { width: 46px; height: 46px; }
  .card--front .brand__name { font-size: 62px; }

  .card--back .brand { right: 40px; top: 34px; }
  .card--back .brand__mark { width: 24px; height: 24px; }
  .card--back .brand__name { font-size: 34px; }

  .divider {
    position: absolute;
    left: 262px; right: 40px; top: 112px;
    height: 1.5px; background: var(--white);
  }
  .person { position: absolute; left: 38px; top: 96px; }
  .person__accent {
    position: absolute; left: -38px; top: 22px;
    width: 12px; height: 34px; background: var(--yellow);
  }
  .person__name {
    font-size: 21px; font-weight: 500; color: var(--yellow);
    letter-spacing: .16em;
  }
  .person__role { font-size: 15px; font-weight: 400; margin-top: 2px; }

  .company { position: absolute; left: 38px; top: 172px; }
  .company__name { font-size: 12.5px; font-weight: 500; color: var(--yellow); letter-spacing: .02em; margin-bottom: 4px; }
  .company__address { font-style: normal; font-size: 13.5px; line-height: 1.42; color: var(--text-soft); }

  .contacts {
    position: absolute; left: 322px; top: 136px;
    list-style: none; font-size: 13.5px; line-height: 1.5; color: var(--text-soft);
  }
  .contacts li { display: flex; align-items: center; gap: 7px; }
  .contacts svg { width: 10px; height: 10px; fill: var(--yellow); flex: none; }
</style>
</head>
<body>

<section class="card card--front" aria-label="Cara frontal">
  <div class="brand">
    <span class="brand__mark"></span>
    <span class="brand__name">VELMIR</span>
  </div>
</section>

<section class="card card--back" aria-label="Cara posterior">
  <div class="brand">
    <span class="brand__mark"></span>
    <span class="brand__name">VELMIR</span>
  </div>

  <div class="divider"></div>

  <div class="person">
    <span class="person__accent"></span>
    <p class="person__name">DARIO FERRAND</p>
    <p class="person__role">Director</p>
  </div>

  <div class="company">
    <p class="company__name">FERREPIEZAS CALIZA, S.R.L.</p>
    <address class="company__address">
      C/ Ramiro Olmedo Lasta<br>
      esquina Tomás Urbina # 47<br>
      Barrio Lucero, Santo Domingo,<br>
      República Dominicana
    </address>
  </div>

  <ul class="contacts">
    <li><svg viewBox="0 0 10 10"><path d="M2 0h2l1 2.5-1.3 1a6 6 0 0 0 2.8 2.8l1-1.3L10 6v2a2 2 0 0 1-2 2A8 8 0 0 1 0 2a2 2 0 0 1 2-2z"/></svg>809.542.4476</li>
    <li><svg viewBox="0 0 10 10"><rect x="2" y="0" width="6" height="3"/><rect x="0" y="3" width="10" height="5" rx="1"/><rect x="2" y="7" width="6" height="3"/></svg>809.594.7361</li>
    <li><svg viewBox="0 0 10 10"><path d="M2.5 0h5a1 1 0 0 1 1 1v8a1 1 0 0 1-1 1h-5a1 1 0 0 1-1-1V1a1 1 0 0 1 1-1zm.5 1.5v6h4v-6z"/></svg>829 746 2158</li>
    <li><svg viewBox="0 0 10 10"><path d="M0 1.5h10v7H0zm1 1v.3L5 5.5l4-2.7v-.3zm0 1.5v3.5h8V4L5 6.7z"/></svg>muestra@muestra.example</li>
    <li><svg viewBox="0 0 10 10"><path d="M0 1.5h10v7H0zm1 1v.3L5 5.5l4-2.7v-.3zm0 1.5v3.5h8V4L5 6.7z"/></svg>muestra@correo-ejemplo.example</li>
    <li><svg viewBox="0 0 10 10"><path d="M5 0a5 5 0 1 0 0 10A5 5 0 0 0 5 0zm0 1a4 4 0 0 1 3.9 3.5H1.1A4 4 0 0 1 5 1zm-3.9 4.5h7.8A4 4 0 0 1 1.1 5.5z"/></svg>www.muestra.example</li>
  </ul>
</section>

</body>
</html>
```